Flyer-Design für Keramik Verdunster
Zielgruppe
Wir wollen Keramik Verdunster bei Volkarn Verkaufen und dieser Flyer soll in jede Produktverpackung mit hinein gelegt werden.
Aufgabenstellung
Der Flyer sollte möglichst klein gehalten werden, also mehrmals Faltbar. Kann auf Vorder- und Rückseite bedruckt werden.
Ihrer Kreativität sind von unserer seite aus ,keine Grenzen gesetzt.
Im Anhang unser Logo , was mit auf den Flyer muss und in der Worddatei haben wir in Klammern noch Instruktionen für sie mit reingeschrieben. Design ect. ist Ihnen überlassen

```html
<!DOCTYPE html>
<html lang="de">
<head>
<meta charset="utf-8">
<title>Larivento – Anleitung für ein ideales Raumklima</title>
<link href="https://fonts.googleapis.com/css2?family=Cabin:wght@400;600;700&display=swap" rel="stylesheet">
<style>
:root{
  --brand-blue:#0a7fc7;
  --heading-blue:#1479c4;
  --panel-light:#e3eaf6;
  --row-tint:#e6f1fb;
  --head-tint:#d5e8f8;
  --ink:#1d1d1b;
  --white:#ffffff;
  --logo-navy:#2b2f86;
}
*{margin:0;padding:0;box-sizing:border-box}
html,body{width:1200px;height:605px;overflow:hidden;background:var(--white)}
body{font-family:"Cabin",Arial,sans-serif;color:var(--ink);position:relative}
.panel{position:absolute}
p{font-size:8px;line-height:10.1px}
.radiator-photo{left:0;top:0;width:249px;height:300px;background:linear-gradient(135deg,#cfcfcf,#f3f3f3 45%,#9e9e9e)}
.note-box{left:0;top:216px;width:249px;height:71px;background:var(--brand-blue);color:var(--white);padding:9px 12px 0 17px}
.instructions{left:249px;top:0;width:298px;height:300px;background:var(--panel-light);padding:30px 22px 0 14px}
.blue-heading{color:var(--heading-blue);font-weight:600;font-size:9.6px;line-height:11.5px}
.instructions ol{list-style:none;margin-top:18px}
.instructions li{font-size:8px;line-height:10.1px;margin-bottom:10.2px}
.sky-photo{left:547px;top:0;width:353px;height:300px;background:linear-gradient(180deg,#3f78bf,#8fb5e0 45%,#d8e6f4 75%,#5a8fd0)}
.airing-box{left:561px;top:55px;width:230px;height:236px;background:rgba(226,234,248,.9);padding:10px 6px 0 6px}
.airing-box .blue-heading{margin-bottom:8px}
.airing-box p{margin-bottom:10.2px}
.months-box{left:797px;top:97px;width:103px;height:159px;background:rgba(236,241,250,.95);padding:8px 0 0 6px}
.months-box h3{font-size:8px;font-weight:600;margin-bottom:10px}
.months-box table{border-collapse:collapse;font-size:8px}
.months-box td{line-height:10.2px;padding:0}
.months-box td:first-child{width:54px}
.logo-panel{left:900px;top:0;width:300px;height:300px;background:var(--white);text-align:center}
.brand-mark{position:absolute;left:1021px;top:127px;width:56px;height:56px;border-radius:50%;background:var(--logo-navy)}
.brand-name{position:absolute;left:900px;width:300px;top:196px;text-align:center;font-size:18px;letter-spacing:5px;font-weight:400;color:var(--ink)}
.brand-tagline{position:absolute;left:900px;width:300px;top:229px;text-align:center;font-size:12.5px;font-weight:600}
.guide{left:15px;top:327px;width:520px}
.guide .lead{margin-top:7px}
.guide h3{font-size:8px;font-weight:700;margin-top:18px}
.guide .intro{margin-top:12px}
.guide .table-title{margin-top:17px;color:var(--heading-blue);font-size:8.4px;font-weight:600}
.climate-table{left:15px;top:469px;width:316px;border-collapse:collapse;font-size:8px}
.climate-table th{background:var(--head-tint);text-align:left;font-weight:600;height:15px;padding-left:4px}
.climate-table td{height:15.3px;padding-left:4px}
.climate-table tr:nth-child(even) td{background:var(--row-tint)}
.kitchen-box{left:343px;top:475px;width:257px;height:106px;background:var(--brand-blue);color:var(--white);padding:12px 13px 0 13px}
.kitchen-box p+p{margin-top:10.2px}
.bedroom-photo{left:600px;top:305px;width:300px;height:300px;background:linear-gradient(160deg,#c9d8b0,#f2f4ec 45%,#e8ecef 70%,#b8c2cc)}
.facts-box{left:625px;top:415px;width:258px;height:163px;background:rgba(10,127,199,.85);color:var(--white);padding:12px 6px 0 13px}
.facts-box h3{font-size:8.2px;font-weight:600;margin-bottom:10px}
.facts-box p{margin-bottom:10.2px}
.review-panel{left:900px;top:305px;width:300px;height:300px;background:var(--panel-light);text-align:center}
.stars{position:absolute;left:1005px;top:406px}
.review-text{position:absolute;left:900px;width:300px;top:447px;text-align:center;font-size:10.5px;font-weight:600;line-height:12.6px;text-transform:uppercase}
.review-text span{display:block;margin-top:13px}
</style>
</head>
<body>
<div class="panel radiator-photo" role="img" aria-label="Weißer Heizkörper mit zwei eingehängten Keramik-Verdunstern"></div>
<div class="panel note-box"><p>Die Verdunstungsdauer hängt von den verschiedensten Faktoren ab. Je gesättigter Ihre relative Luftfeuchtigkeit im Raum (durch schlechtes Lüften) und je kälter der Heizkörper desto Länger dauert der Verdunstungsprozess! Die Luft kann dadurch nicht mehr Feuchtigkeit aufnehmen!</p></div>

<section class="panel instructions">
  <h2 class="blue-heading">Was muss ich beachten und wie funktionieren meine neuen Larivento Heizkörper Luftbefeuchter.</h2>
  <ol>
    <li>1. Füllen Sie Ihre neuen Luftbefeuchter mit warmen Wasser, idealerweise mit entkalktem Wasser.</li>
    <li>2. Sollten Sie kein entkalktes Wasser haben , sollten Sie Ihre Verdunster nach jedem Durchgang (Komplett Verdunstet) mit verdünntem Essig oder Zitronensäure von innen reinigen, um die Poren Kalkfrei zu halten und um eine optimale Verdunstung zu gewährleisten.</li>
    <li>3. Um weiterhin eine optimale Verdunstung zu gewährleisten, sollte Ihr Heizkörper so warm sein, dass Sie ihn gerade noch mit der Hand anfassen können oder noch heißer.</li>
    <li>4. Bringen Sie an jedem Heizkörper zwei Verdunster an. Außer im Bad und der Küche!</li>
    <li>5. Wenn die Verdunster zu lange an einem Heizkörper hängen, die abgeschaltet bzw. kalt sind ,dann kann es zur Tröpfchenbildung kommen, weil die Poren groß sind und bei kalter Oberfläche kann das Wasser nicht schnell genug verdunsten.</li>
  </ol>
</section>

<div class="panel sky-photo" role="img" aria-label="Blauer Himmel mit Wolken und fliegender Möwe"></div>
<section class="panel airing-box">
  <h2 class="blue-heading">Richtiges Lüften</h2>
  <p>Schließen Sie den Thermostatkopf der Heizungen komplett. Öffnen Sie die Fenster zweier gegenüberliegender Räume gleichzeitig und lassen auch die Türen offen stehen.</p>
  <p>Auf diese Weise entsteht ein Durchzug und die warme, verbrauchte Luft zieht schneller nach draußen ab.</p>
  <p>Achtung: Vergessen Sie nicht, auch im zweiten Raum, den Heizkörper während des Lüftens abzustellen!</p>
  <p>Wie oft sollten Sie Lüften? Optimal wäre 4 mal am Tag, da dies aber oft nicht möglich ist, sollten Sie mindestens 2 mal am Tag Lüften, Abends vor dem Schlafen gehen und Morgens nach dem Aufstehen.</p>
  <p>Wenn Sie nun so vorgehen wie beschrieben, wird Ihnen und dem wunderbaren Gefühl eines schönen Klimas im Zuhause, nichts mehr im Wege stehen.</p>
</section>
<section class="panel months-box">
  <h3>Dauer des Lüftens:</h3>
  <table>
    <tr><td>Januar</td><td>5 min</td></tr>
    <tr><td>Februar</td><td>5 min</td></tr>
    <tr><td>März</td><td>10 min</td></tr>
    <tr><td>April</td><td>15 min</td></tr>
    <tr><td>Mai</td><td>20 min</td></tr>
    <tr><td>Juni</td><td>30 min</td></tr>
    <tr><td>Juli</td><td>30 min</td></tr>
    <tr><td>August</td><td>30 min</td></tr>
    <tr><td>September</td><td>15 min</td></tr>
    <tr><td>Obtober</td><td>20 min</td></tr>
    <tr><td>November</td><td>10 min</td></tr>
    <tr><td>Dezember</td><td>5 min</td></tr>
  </table>
</section>

<div class="panel logo-panel"></div>
<div class="brand-mark"></div>
<div class="brand-name">LARIVENTO</div>
<div class="brand-tagline">Anleitung für ein ideales Raumklima</div>

<section class="panel guide">
  <h2 class="blue-heading">Anleitung für ein Ideales Raumklima und die optimale<br>Luftfeuchtigkeit mit Ihrem Larivento Heizkörper Luftbefeuchter!</h2>
  <p class="lead">Für ein schönes Klima sorgen Sie, wie Folgt:</p>
  <h3>relative Luftfeuchtigkeit in Wohnräumen</h3>
  <p class="intro">In der folgenden Tabelle finden Sie die optimalen Werte für relative Luftfeuchte und Temperatur in den verschiedenen Wohnbereichen.<br>Als ideale Mittelwerte haben sich 40 - 60 % Feuchte und 20 °C Raumtemperatur bewährt.</p>
  <p class="table-title">Ideales Raumklima</p>
</section>
<table class="panel climate-table">
  <tr><th>Raum</th><th>Optimale Temperatur</th><th>Optimale Luftfeuchtigkeit</th></tr>
  <tr><td>Wohnräume</td><td>20 °C</td><td>40 - 60 %</td></tr>
  <tr><td>Schlafzimmer</td><td>16 - 18 °C</td><td>40 - 60 %</td></tr>
  <tr><td>Kinderzimmer</td><td>20 - 22 °C</td><td>40 - 60 %</td></tr>
  <tr><td>Küche</td><td>18 °C</td><td>50 - 60 %</td></tr>
  <tr><td>Badezimmer</td><td>23 °C</td><td>50 - 70 %</td></tr>
  <tr><td>Keller</td><td>10 - 15 °C</td><td>50 - 65 %</td></tr>
</table>
<section class="panel kitchen-box">
  <p>Naturgemäß liegt die Luftfeuchte in Küche und Bad etwas höher und kann beim Kochen oder Duschen auch über diese Werte steigen.</p>
  <p>Das ist kein Problem, solange der Zustand nicht dauerhaft anhält. Dennoch sollte es Ihnen zur Gewohnheit werden, sofort nach dem Kochen oder Duschen den Wasserdampf nach draußen entweichen zu lassen.</p>
</section>

<div class="panel bedroom-photo" role="img" aria-label="Helles Schlafzimmer mit schlafender Person vor grünem Hintergrund"></div>
<section class="panel facts-box">
  <h3>Wissenswertes zur Luftfeuchtigkeit</h3>
  <p>Das gesündeste Raumklima herrscht bei 50 % relativer<br>Luftfeuchte und 20 °C Raumtemperatur.</p>
  <p>Die relative Raumfeuchte sollte nicht unter 30 % fallen.</p>
  <p>Einige Schimmelpilzarten vermehren sich bereits<br>ab 70 % Feuchtigkeit.</p>
  <p>Herrschen über einen längeren Zeitraum mehr als 80 % Feuchtigkeit im Raum, führt das unvermeidlich zur Entstehung von Schimmel.</p>
</section>

<div class="panel review-panel"></div>
<svg class="stars" width="78" height="14" viewBox="0 0 78 14" aria-label="Fünf Sterne">
  <g fill="#1d1d1b">
    <polygon id="s" points="7,0 8.7,4.9 13.8,5 9.7,8.1 11.2,13 7,10.1 2.8,13 4.3,8.1 0.2,5 5.3,4.9"/>
    <use href="#s" x="15.5"/><use href="#s" x="31"/><use href="#s" x="46.5"/><use href="#s" x="62"/>
  </g>
</svg>
<div class="review-text">Sie sind zufrieden mit unserem Produkt<br>und dieser Anleitung?<span>Dann hinterlassen Sie uns doch bitte<br>eine Rezension auf Volkarn.</span></div>
</body>
</html>
```